Birchline Heating & Air

I need a business card made for my company. I would like my new logo for Birchline Heating and Air on the front and my Garage Door on the back.
Front to say -Heating & Air Conditioning , Mini Splits and Heat Pumps, Hydronic In-Floor Heat. Locally Owned and Operated! Licensed, Boned and Insured. Free Estimates on new equipment. 715-408-2159
BGD Back Card, change phone# to 651-374-5810. Remove Commercial and residential and fully sticked vans lines.

```html
<!DOCTYPE html>
<html lang="en">
<head>
<meta charset="utf-8">
<title>Birchline Heating &amp; Air — Business Card</title>
<link href="https://fonts.googleapis.com/css2?family=Lato:wght@400;700;900&display=swap" rel="stylesheet">
<style>
  :root {
    --brand-blue: #0f4f87;
    --brand-red: #ef2a16;
    --card-white: #ffffff;
    --backdrop: #3a3a3c;
  }
  * { box-sizing: border-box; margin: 0; padding: 0; }
  html, body {
    width: 1200px; height: 875px; overflow: hidden;
    background: var(--backdrop);
    font-family: "Lato", sans-serif;
  }
  .canvas { position: relative; width: 1200px; height: 875px; }
  .card {
    position: absolute; left: 250px; width: 700px; height: 400px;
    border-radius: 22px; overflow: hidden; background: var(--card-white);
  }
  .card--front { top: 25px; }
  .card--back { top: 450px; }

  /* Front */
  .front-logo {
    position: absolute; top: 30px; left: 0; right: 0;
    display: flex; flex-direction: column; align-items: center;
    color: var(--brand-blue); font-weight: 900; text-transform: uppercase;
  }
  .front-logo .logo-name {
    display: flex; align-items: center; gap: 14px;
    font-size: 52px; line-height: 1; letter-spacing: 1px;
  }
  .front-logo .mark {
    width: 34px; height: 34px; border-radius: 50%; background: var(--brand-red); flex: none;
  }
  .front-logo .logo-sub {
    margin-top: 8px; font-size: 30px; line-height: 1; letter-spacing: 1px;
  }
  .service-band {
    position: absolute; top: 146px; left: 0; right: 0; height: 88px;
    background: var(--brand-blue); color: var(--card-white);
    display: flex; flex-direction: column; justify-content: center; align-items: center;
    font-weight: 900; font-size: 19px; line-height: 1.45; text-align: center;
  }
  .front-contact { position: absolute; top: 256px; left: 0; right: 0; text-align: center; }
  .front-contact .estimate { color: var(--brand-red); font-weight: 900; font-size: 19px; line-height: 1.2; }
  .front-contact .phone { color: var(--brand-red); font-weight: 900; font-size: 58px; line-height: 1.05; }
  .front-contact .web { color: var(--brand-blue); font-weight: 700; font-size: 22px; letter-spacing: 2px; line-height: 1.2; }

  /* Back */
  .back-panel { position: absolute; top: 0; bottom: 0; left: 0; width: 440px; background: var(--brand-blue); }
  .back-divider { position: absolute; top: 0; bottom: 0; left: 452px; width: 7px; background: var(--brand-red); }
  .back-details { position: absolute; top: 62px; left: 52px; color: var(--card-white); }
  .back-details .name { font-weight: 900; font-size: 34px; letter-spacing: 1px; text-transform: uppercase; line-height: 1.1; }
  .back-details .phone { font-weight: 900; font-size: 40px; line-height: 1.1; }
  .back-details .email { font-style: italic; font-size: 19px; margin-top: 2px; }
  .back-details .features { list-style: none; margin-top: 22px; font-size: 22px; line-height: 1.45; }
  .back-details .features li::before {
    content: ""; display: inline-block; width: 9px; height: 9px; border-radius: 50%;
    background: var(--card-white); margin-right: 12px; vertical-align: middle;
  }
  .back-details .visit { margin-top: 22px; font-weight: 900; font-size: 17px; text-transform: uppercase; }
  .back-details .site { font-weight: 900; font-size: 28px; }
  .back-logo {
    position: absolute; top: 0; bottom: 0; left: 459px; right: 0;
    display: flex; flex-direction: column; align-items: center; justify-content: center;
    color: var(--brand-blue); font-weight: 900; font-size: 34px;
    text-transform: uppercase; text-align: center; line-height: 1.1;
  }
  .back-logo .mark { width: 30px; height: 30px; background: var(--brand-red); margin-bottom: 14px; }
</style>
</head>
<body>
<main class="canvas">
  <section class="card card--front" aria-label="Card front">
    <div class="front-logo">
      <p class="logo-name"><span class="mark"></span>Birchline</p>
      <p class="logo-sub">Heating &amp; Air</p>
    </div>
    <div class="service-band">
      <p>Heating &amp; Air Conditioning | Mini Splits &amp; Heat Pumps | Hydronic In-Floor Heat</p>
      <p>Locally Owned &amp; Operated! | Licensed, Boned &amp; Insured.</p>
    </div>
    <div class="front-contact">
      <p class="estimate">Free Estimates on new equipment.</p>
      <p class="phone">715-408-2159</p>
      <p class="web">www.BirchlineHeatingandAir.com</p>
    </div>
  </section>

  <section class="card card--back" aria-label="Card back">
    <div class="back-panel"></div>
    <div class="back-divider"></div>
    <div class="back-details">
      <p class="name">Ray Calloway</p>
      <p class="phone">651-374-5810</p>
      <p class="email">birchlinegaragedoor@mailbox.com</p>
      <ul class="features">
        <li>Same Day &amp; Emergency Service</li>
        <li>All Major Brands</li>
        <li>Locally Owned &amp; Operated</li>
      </ul>
      <p class="visit">Visit our website!</p>
      <p class="site">BirchlineGarageDoor.com</p>
    </div>
    <div class="back-logo">
      <div class="mark"></div>
      <p>Birchline<br>Garage Door</p>
    </div>
  </section>
</main>
</body>
</html>
```